Complimentary Plantix View promotional postcard for a chiropractor

I am a chiropractor who is looking to have a postcard designed to promote complimentary Plantix Views. The answer to being pain free could be right under your feet!A Plantix View will detect if gait or foot imbalances are the cause of:Foot or Heel painLow back painKnee painShin painMy credentials that should appear on the card are: Dr. Marla Tendwick B.Sc., D.C.575 River Glen Blvd. Unit 7Oakville, ONL6H 6X6905-257-5888

Target Market(s)

30-50 year olds - white collar

Industry/Entity Type

Chiropractor

Font styles to use
Serif

Colors
34a6d7

Requirements
Must have
• a line where I can hand write an expiry date
• white background
• dark grey letttering (not black)
• The words " Bring this postcard in to receive a complimentary Plantix View with Dr. Marla Tendwick. Please call to book an appointment.
• white back ground
Should not have
• clutter - or too much to read
• The Marbrook group - please use "custom orthotics" instead
• no stock images
• no other images except company logo and Plnatix View images

```html
<!DOCTYPE html>
<html lang="en">
<head>
<meta charset="utf-8">
<title>Plantix View Postcard</title>
<link href="https://fonts.googleapis.com/css2?family=Questrial&display=swap" rel="stylesheet">
<style>
  :root {
    --stage: #3a3a3a;
    --card: #ffffff;
    --brand-blue: #34a6d7;
    --deep-blue: #1f6f99;
    --ink-grey: #4a4a4a;
    --logo-grey: #7a7a7a;
    --stamp-grey: #a7a7a7;
  }
  * { box-sizing: border-box; margin: 0; padding: 0; }
  html, body { width: 900px; height: 1200px; overflow: hidden; }
  body {
    background: var(--stage);
    font-family: "Questrial", "Century Gothic", sans-serif;
    position: relative;
  }
  .postcard {
    position: absolute;
    left: 97px;
    width: 689px;
    height: 530px;
    background: var(--card);
    overflow: hidden;
  }
  .postcard--front { top: 47px; }
  .postcard--back { top: 618px; }

  /* Front */
  .front-copy {
    position: absolute; left: 0; top: 0; width: 378px; height: 100%;
    text-align: center;
  }
  .brand {
    position: absolute; top: 112px; left: 0; width: 100%;
    display: flex; flex-direction: column; align-items: center;
  }
  .brand-mark {
    width: 24px; height: 24px; border-radius: 50%;
    background: var(--brand-blue); margin-bottom: 16px;
  }
  .brand-name {
    color: var(--logo-grey); font-size: 21px; letter-spacing: 0.5px;
    text-transform: uppercase; line-height: 1.1;
  }
  .brand-sub {
    color: var(--logo-grey); font-size: 14px; letter-spacing: 2.5px;
    text-transform: uppercase;
  }
  .headline {
    position: absolute; top: 214px; left: 0; width: 100%;
    font-size: 24px; line-height: 1.22; font-weight: 400;
  }
  .headline-lead { color: var(--brand-blue); display: block; }
  .headline-strong { color: var(--deep-blue); display: block; font-weight: 700; }
  .intro {
    position: absolute; top: 293px; left: 28px; width: 325px;
    text-align: left; color: var(--ink-grey); font-size: 14px; line-height: 1.3;
  }
  .symptoms {
    position: absolute; top: 344px; left: 24px; list-style: none; text-align: left;
  }
  .symptoms li {
    color: var(--deep-blue); font-size: 26px; line-height: 31.5px;
    display: flex; align-items: center;
  }
  .symptoms li::before {
    content: ""; width: 12px; height: 12px; border-radius: 50%;
    background: var(--brand-blue); margin-right: 14px;
  }
  .web {
    position: absolute; top: 480px; left: 0; width: 100%;
    color: var(--brand-blue); font-size: 23px;
  }
  .front-visual {
    position: absolute; left: 378px; top: 0; width: 311px; height: 100%;
    background: radial-gradient(ellipse at 55% 35%, #c9825a 0%, #4a7fb0 18%, #2a5a8f 55%, #183e6a 100%);
  }

  /* Back */
  .scan-visual {
    position: absolute; left: 63px; top: 110px; width: 256px; height: 120px;
    border-radius: 8px;
    background: radial-gradient(ellipse at 45% 45%, #3d6e9c 0%, #26303c 45%, #1c1c1e 100%);
  }
  .offer {
    position: absolute; left: 45px; top: 248px; width: 310px;
    color: var(--ink-grey); font-size: 13px; line-height: 17px;
  }
  .expiry {
    position: absolute; left: 45px; top: 306px;
    color: var(--ink-grey); font-size: 13px;
    display: flex; align-items: flex-end;
  }
  .expiry-line {
    display: inline-block; width: 150px; margin-left: 8px;
    border-bottom: 1px solid var(--ink-grey); height: 13px;
  }
  .divider {
    position: absolute; left: 379px; top: 87px; width: 2px; height: 365px;
    background: var(--ink-grey);
  }
  .stamp {
    position: absolute; left: 553px; top: 54px; width: 90px; height: 110px;
    background: var(--stamp-grey);
  }
  .sender { position: absolute; left: 45px; top: 338px; }
  .sender-name { color: var(--deep-blue); font-size: 23px; margin-bottom: 16px; }
  .sender-address { font-style: normal; color: var(--brand-blue); font-size: 19.5px; line-height: 22px; }
  .sender-phone { color: var(--deep-blue); }
</style>
</head>
<body>
  <section class="postcard postcard--front">
    <div class="front-copy">
      <div class="brand">
        <span class="brand-mark"></span>
        <span class="brand-name">Fernridge Wellness</span>
        <span class="brand-sub">Health Centres</span>
      </div>
      <h1 class="headline">
        <span class="headline-lead">The answer to being pain free</span>
        <span class="headline-strong">could be right under your feet!</span>
      </h1>
      <p class="intro">A Plantix View will detect if gait or foot imbalances are the cause of:</p>
      <ul class="symptoms">
        <li>Foot or Heel pain</li>
        <li>Low back pain</li>
        <li>Knee pain</li>
        <li>Shin pain</li>
      </ul>
      <p class="web">www.fernridgewellness.com</p>
    </div>
    <div class="front-visual" role="img" aria-label="Illustration of a translucent human back showing the spine and ribs with the spine highlighted in red"></div>
  </section>

  <section class="postcard postcard--back">
    <div class="scan-visual" role="img" aria-label="Photo of the Plantix View pressure plate showing a colour footprint scan"></div>
    <p class="offer">Bring this postcard in to receive a complimentary Plantix View with Dr. Marla Tendwick. Please call to book an appointment.</p>
    <p class="expiry">Expires:<span class="expiry-line"></span></p>
    <div class="divider"></div>
    <div class="stamp"></div>
    <div class="sender">
      <p class="sender-name">Dr. Marla Tendwick B.Sc., D.C.</p>
      <address class="sender-address">
        218 Cedarholm Ave. Unit 3<br>
        Oakville, ON<br>
        L4K 2P9<br>
        <span class="sender-phone">905-555-0143</span>
      </address>
    </div>
  </section>
</body>
</html>
```